Business Card Design Project

Refresh of logo attached. Require text underneath to be more ledgible, crisper & cleaner.

Overall, staying with same colour scheme need a brighter, crisper, easily readible business card style.

Industry/Entity Type

Business

```html
<!DOCTYPE html>
<html lang="en">
<head>
<meta charset="utf-8">
<title>Business Card – Daniel R. Whitfield</title>
<link href="https://fonts.googleapis.com/css2?family=Jost:wght@400;600&family=Tinos:wght@700&display=swap" rel="stylesheet">
<style>
  :root {
    --band-top: #2b97b7;
    --band-bottom: #1e4f62;
    --card-bg: #ffffff;
    --ink: #111111;
    --accent: #2b97b7;
  }
  html, body {
    margin: 0;
    padding: 0;
    overflow: hidden;
    background: var(--card-bg);
  }
  .card {
    position: relative;
    width: 1200px;
    height: 693px;
    background: var(--card-bg);
    overflow: hidden;
  }
  .band {
    position: absolute;
    left: 0;
    width: 100%;
  }
  .band--top {
    top: 0;
    height: 116px;
    background: var(--band-top);
  }
  .band--bottom {
    bottom: 0;
    height: 116px;
    background: var(--band-bottom);
  }
  .identity {
    position: absolute;
    left: 0;
    width: 100%;
    text-align: center;
    color: var(--ink);
    margin: 0;
  }
  .identity__name {
    top: 219px;
    font-family: "Tinos", "Times New Roman", serif;
    font-weight: 700;
    font-size: 52px;
    line-height: 1;
    letter-spacing: -0.3px;
  }
  .identity__title {
    top: 273px;
    font-family: "Jost", sans-serif;
    font-weight: 400;
    font-size: 35px;
    line-height: 1;
  }
  .contact {
    position: absolute;
    left: 443px;
    top: 327px;
    margin: 0;
    font-family: "Jost", sans-serif;
    font-size: 35px;
    line-height: 43.5px;
    color: var(--ink);
  }
  .contact__row {
    display: flex;
    margin: 0;
  }
  .contact__label {
    width: 65px;
    font-weight: 600;
    color: var(--accent);
  }
  .contact__value {
    margin: 0;
    font-weight: 400;
  }
</style>
</head>
<body>
  <main class="card">
    <div class="band band--top"></div>

    <h1 class="identity identity__name">Daniel R. Whitfield</h1>
    <p class="identity identity__title">Registered Estate Consultant</p>

    <dl class="contact">
      <div class="contact__row">
        <dt class="contact__label">T:</dt>
        <dd class="contact__value">(416) 555 0147</dd>
      </div>
      <div class="contact__row">
        <dt class="contact__label">M:</dt>
        <dd class="contact__value">(647) 555 0183</dd>
      </div>
      <div class="contact__row">
        <dt class="contact__label">E:</dt>
        <dd class="contact__value">daniel@execadvise.ca</dd>
      </div>
    </dl>

    <div class="band band--bottom"></div>
  </main>
</body>
</html>
```